Brookfell Self Storage - Business Sign

The sign we are needing designed is our main road sign for our self-storage business. The dimensions of the sign are 57 inches tall x 96 inches wide. We require that our attached logo be on the sign as well as our phone number: 478-216-4387 and website www.BrookfellStorage.net. Optional information that can be added but not required is our address: 418 Marlow Tenney Pkwy, Centerville, GA 31047.

Industry/Entity Type

Self Storage

Font styles to use
Sans Serif

```html
<!DOCTYPE html>
<html lang="en">
<head>
<meta charset="UTF-8">
<title>Brookfell Self Storage – Road Sign</title>
<link href="https://fonts.googleapis.com/css2?family=Montserrat:wght@600;800&family=Oswald:wght@500&display=swap" rel="stylesheet">
<style>
  :root {
    --page: #e9edf2;
    --sign: #f4f4f4;
    --ink: #3a3a3c;
    --ink-soft: #6b6b6e;
    --brand-blue: #1e7fe0;
    --brand-blue-light: #45a6ee;
    --photo-sky: #2f82d6;
    --photo-doors: #1f6fd0;
    --photo-ground: #5b5e63;
  }
  * { margin: 0; padding: 0; box-sizing: border-box; }
  html, body {
    width: 1200px; height: 1100px; overflow: hidden;
    background: var(--page);
  }
  .sign {
    position: absolute; left: 40px; top: 217px;
    width: 1120px; height: 665px;
    background: var(--sign);
    overflow: hidden;
    box-shadow: 0 10px 30px rgba(0,0,0,.15);
  }
  .sign-art { position: absolute; inset: 0; }
  .brand {
    position: absolute; left: 693px; width: 400px; top: 190px;
    text-align: center;
    font-family: "Montserrat", sans-serif;
    color: var(--ink);
    line-height: 1.1;
  }
  .brand-name { display: block; font-size: 72px; font-weight: 800; letter-spacing: 1px; }
  .brand-tag {
    display: block; font-size: 32px; font-weight: 600;
    letter-spacing: 7px; margin-top: 4px; color: var(--ink-soft);
  }
  .divider {
    position: absolute; left: 706px; top: 400px;
    width: 414px; height: 2px; background: var(--brand-blue);
  }
  .website {
    position: absolute; right: 27px; top: 464px;
    font-family: "Oswald", sans-serif; font-weight: 500;
    font-size: 34px; line-height: 1.2; letter-spacing: .3px;
    color: var(--ink); text-transform: uppercase;
    white-space: nowrap;
  }
  .website .domain { color: var(--brand-blue); }
  .phone {
    position: absolute; right: 27px; top: 515px;
    display: flex; align-items: center; gap: 14px;
    font-family: "Montserrat", sans-serif; font-weight: 800;
    font-size: 60px; line-height: 1.1; color: var(--ink); letter-spacing: -1px;
    white-space: nowrap;
  }
  .phone-icon { width: 56px; height: 56px; flex: none; }
</style>
</head>
<body>
  <main class="sign">
    <svg class="sign-art" width="1120" height="665" viewBox="0 0 1120 665">
      <defs>
        <linearGradient id="photoTone" x1="0" y1="0" x2="0" y2="1">
          <stop offset="0" stop-color="var(--photo-sky)"/>
          <stop offset=".42" stop-color="#3b8fdc"/>
          <stop offset=".5" stop-color="var(--photo-doors)"/>
          <stop offset=".66" stop-color="var(--photo-doors)"/>
          <stop offset=".72" stop-color="var(--photo-ground)"/>
          <stop offset="1" stop-color="#4e5156"/>
        </linearGradient>
        <linearGradient id="swooshTone" x1="0" y1="0" x2="0" y2="1">
          <stop offset="0" stop-color="var(--brand-blue-light)"/>
          <stop offset="1" stop-color="var(--brand-blue)"/>
        </linearGradient>
      </defs>
      <path class="photo-area" role="img" aria-label="Photo of a row of blue roll-up storage unit doors under a blue sky with trees"
            d="M0,0 L492,0 C600,150 660,400 383,665 L0,665 Z" fill="url(#photoTone)"/>
      <path class="swoosh-band"
            d="M510,0 L560,0 C690,180 700,450 390,628 C660,450 660,180 510,0 Z"
            fill="url(#swooshTone)"/>
    </svg>

    <h1 class="brand">
      <span class="brand-name">Brookfell</span>
      <span class="brand-tag">SELF STORAGE</span>
    </h1>

    <div class="divider"></div>

    <p class="website">www.<span class="domain">BrookfellStorage</span>.net</p>

    <p class="phone">
      <svg class="phone-icon" viewBox="0 0 54 54" aria-hidden="true">
        <circle cx="27" cy="27" r="27" fill="var(--brand-blue)"/>
        <path d="M19 14c1.5-1 3-.6 3.8.8l2.6 4.6c.7 1.3.3 2.6-.8 3.4l-1.8 1.3c1.2 3 3.6 5.6 6.6 7l1.4-1.7c.9-1.1 2.3-1.3 3.5-.5l4.4 2.9c1.3.9 1.6 2.4.6 3.8l-1.6 2.2c-1.2 1.6-3.4 2.2-5.4 1.5C23.5 36.6 17 30 14.4 21.3c-.6-2 .1-4.2 1.8-5.4z"
              fill="#fff"/>
      </svg>
      478-216-4387
    </p>
  </main>
</body>
</html>
```